Labels designs for a new coffee brand (Velloru Coffee)

We looking for a coffee label design for our coffee Brand, VELLORU COFFE, attached is the logo. We are bringing out to the market 3 Premium blends
1. Colombian Popayan
2. Gourmet Expresso Blend
3. Brazilian Santos

We like something that looks high quality yet modern, the bags we are using is black matte, we are starting with labels and look in the near future to print our own labels .

We want the labels for the 3 coffees to have the similar look and feel but to be uniquely identified by its design (Colombian, Brazilian, espresso) This is beig sold as a set so we want it to have a similar label feeling but that each is identify as its unique product (colombian, expresso, brazilian blend.

This project is for labels that will be used on a black matte bag, is for a 16 oz bag,

Attached is a sample of the bag color.

Size Requirements:
Maintain a 2:3 aspect ratio for the image file
The label will be 4" wide and 6" tall (we also want to print some 3X4)
Recommended image size is 1600px X 2400px

I will provide upc later

www.vellorucoffee.example pw 12345 this is the test site not live yet but you can get a feel of the brand

Ay my daughters volleyball tournament I need extra time to review

coffee drinkers

coffee

• Creativity, unique, eye catchy,

```html
<!DOCTYPE html>
<html lang="en">
<head>
<meta charset="utf-8">
<title>Velloru Coffee – Gourmet Expresso Label</title>
<link rel="stylesheet" href="https://fonts.googleapis.com/css2?family=Archivo:wght@400;600&family=Barlow+Condensed:wght@700&display=swap">
<style>
  :root {
    --backdrop: #a2a597;
    --rust: #99432a;
    --rust-deep: #7f3220;
    --rust-light: #a9553a;
    --ink: #151111;
    --peach: #f0c3a8;
  }
  html, body {
    margin: 0;
    width: 1200px;
    height: 900px;
    overflow: hidden;
    background: var(--backdrop);
  }
  .label {
    position: absolute;
    left: 347px;
    top: 40px;
    width: 505px;
    height: 820px;
    box-shadow: 0 10px 30px rgba(0,0,0,0.25);
  }
  .label svg { display: block; }
  .headline {
    font-family: "Barlow Condensed", "Arial Narrow", sans-serif;
    font-weight: 700;
    font-size: 58px;
    fill: var(--ink);
  }
  .brand-name {
    font-family: "Archivo", Arial, sans-serif;
    font-weight: 600;
    font-size: 84px;
    fill: var(--rust);
  }
  .badge-big {
    font-family: "Archivo", Arial, sans-serif;
    font-weight: 600;
    font-size: 30px;
    fill: var(--peach);
  }
  .badge-small {
    font-family: "Archivo", Arial, sans-serif;
    font-weight: 400;
    fill: var(--rust-light);
  }
  .notes-title {
    font-family: "Archivo", Arial, sans-serif;
    font-weight: 400;
    font-size: 22px;
    fill: var(--ink);
  }
  .notes-item, .net-weight {
    font-family: "Archivo", Arial, sans-serif;
    font-weight: 400;
    font-size: 14px;
    fill: var(--ink);
  }
  .net-weight { font-weight: 600; font-size: 14px; }
  .table-line { stroke: var(--ink); stroke-width: 2; fill: none; }
</style>
</head>
<body>
  <div class="label">
    <svg width="505" height="820" viewBox="0 0 505 820">
      <defs>
        <linearGradient id="panelTone" x1="0" y1="0" x2="1" y2="1">
          <stop offset="0" stop-color="#8a3923"/>
          <stop offset="0.5" stop-color="#9b452b"/>
          <stop offset="1" stop-color="#8c3a22"/>
        </linearGradient>
        <pattern id="zigzag" width="10" height="14" patternUnits="userSpaceOnUse">
          <path d="M10 0 L0 7 L10 14 Z" fill="#151111"/>
        </pattern>
      </defs>

      <!-- rust panel with botanical artwork area -->
      <rect class="artwork" role="img" aria-label="Line illustration of coffee branches, leaves and scattered coffee beans" x="0" y="0" width="400" height="820" fill="url(#panelTone)"/>

      <!-- black brand strip with serrated edge -->
      <rect class="brand-strip" x="398" y="0" width="107" height="820" fill="var(--ink)"/>
      <rect class="serrated-edge" x="389" y="0" width="10" height="820" fill="url(#zigzag)"/>

      <!-- brand: plain square + name -->
      <rect class="brand-square" x="434" y="120" width="40" height="40" fill="var(--rust)"/>
      <text class="brand-name" transform="translate(424 236) rotate(90)" x="0" y="0" textLength="516" lengthAdjust="spacing">VELLORU</text>

      <!-- product name -->
      <text class="headline" x="388" y="364" text-anchor="end">GOURMET</text>
      <text class="headline" x="352" y="424" text-anchor="end">EXPRESSO</text>

      <!-- roast badge -->
      <polygon class="roast-badge" fill="var(--ink)" points="360,535 342.1,549.5 350.4,571 327.6,574.6 324,597.4 302.5,589.1 288,607 273.5,589.1 252,597.4 248.4,574.6 225.6,571 233.9,549.5 216,535 233.9,520.5 225.6,499 248.4,495.4 252,472.6 273.5,480.9 288,463 302.5,480.9 324,472.6 327.6,495.4 350.4,499 342.1,520.5"/>
      <text class="badge-big" x="288" y="522" text-anchor="middle">100%</text>
      <text class="badge-small" x="288" y="545" text-anchor="middle" font-size="16">ROASTED</text>
      <text class="badge-small" x="288" y="568" text-anchor="middle" font-size="21">COFFEE</text>

      <!-- cup notes table -->
      <rect class="table-line" x="90" y="633" width="288" height="115"/>
      <line class="table-line" x1="278" y1="633" x2="278" y2="748"/>
      <line class="table-line" x1="90" y1="669" x2="278" y2="669"/>
      <line class="table-line" x1="90" y1="695" x2="278" y2="695"/>
      <line class="table-line" x1="90" y1="721" x2="278" y2="721"/>
      <text class="notes-title" x="98" y="660">CUP NOTES</text>
      <text class="notes-item" x="98" y="688">ORANGE CITRUS</text>
      <text class="notes-item" x="98" y="714">DARK CARAMEL</text>
      <text class="notes-item" x="98" y="740">BAKERS CHOCOLATE</text>

      <text class="net-weight" x="94" y="782">NET WEIGHT | 16 OZ</text>
    </svg>
  </div>
</body>
</html>
```